Harbourline Physiotherapy business card design

We need a fresh, new business card design for our physiotherapy clinic Harbourline Physiotherapy

Will attach logo soon we had logo designed from our last project

Industry/Entity Type

Physical Therapy

Contact Information for Business Card

On front
Needs our logo, contact details:
48 Wexford Lane Kellyvale NSW 2791
Ph/f: 02 9481 2057
info@harbourlinephysio.example.com.au

Requirements
Must have
• On the back of the card needs to have area to write down follow up appointments
• On front
• Needs our logo
• The colours have to be the colours in our logo which are: sky blue, black and white
• Font to be same as our logo please
• We want the card to look simple, not too cluttered but to the point
Should not have
• We don't need any extra pictures other than our logo

```html
<!DOCTYPE html>
<html lang="en">
<head>
<meta charset="utf-8">
<title>Harbourline Physiotherapy – Business Card</title>
<link href="https://fonts.googleapis.com/css2?family=Open+Sans:wght@400;600;700&display=swap" rel="stylesheet">
<style>
  :root {
    --sky: #2a6fd0;
    --sky-deep: #1d4fb0;
    --sky-light: #4a9be4;
    --ink: #3a3a3a;
    --muted: #8a8a8a;
    --rule: #7fa6dc;
    --paper: #ffffff;
    --backdrop: #e8e6e2;
    --font: "Open Sans", Arial, sans-serif;
  }
  * { box-sizing: border-box; margin: 0; padding: 0; }
  html, body { width: 1200px; height: 843px; overflow: hidden; }
  body { background: var(--backdrop); font-family: var(--font); position: relative; }

  .card {
    position: absolute;
    width: 600px; height: 343px;
    background: var(--paper);
    box-shadow: 0 6px 18px rgba(0,0,0,.18);
    overflow: hidden;
  }

  /* ---------- Appointment side ---------- */
  .card--back { left: 50px; top: 70px; }
  .card--back .watermark {
    position: absolute; left: 20px; top: 70px;
    width: 190px; height: 190px; border-radius: 50%;
    background: radial-gradient(circle, rgba(42,111,208,.10), rgba(42,111,208,0));
  }
  .appt-title {
    position: absolute; right: 40px; top: 26px;
    color: var(--sky); font-weight: 700; font-size: 22px;
  }
  .appt-row {
    position: absolute; left: 40px; right: 40px;
    display: flex; align-items: flex-end; gap: 8px;
    color: var(--sky); font-size: 15px;
  }
  .appt-row .label { white-space: nowrap; }
  .appt-row .line { flex: 1; border-bottom: 1.5px dotted var(--rule); height: 14px; }
  .appt-row .ampm { font-size: 11px; color: var(--sky); align-self: flex-start; }
  .row-name { top: 88px; }
  .row-date { top: 128px; }
  .row-days { top: 172px; justify-content: space-between; }
  .row-note { top: 214px; }
  .row-note2 { top: 246px; left: 40px; }
  .day { display: flex; align-items: center; gap: 6px; }
  .tick-box { width: 14px; height: 12px; border: 1.3px solid var(--ink); background: #fff; }
  .appt-footnote {
    position: absolute; left: 0; right: 0; bottom: 34px;
    text-align: center; color: var(--muted); font-size: 11px;
  }

  /* ---------- Contact side ---------- */
  .card--front { left: 560px; top: 400px; }
  .brand {
    position: absolute; left: 0; right: 0; top: 52px;
    display: flex; justify-content: center; align-items: center; gap: 12px;
  }
  .brand .dot { width: 34px; height: 34px; border-radius: 50%; background: var(--sky); }
  .brand .name { color: var(--sky); font-weight: 700; font-size: 26px; }
  .band {
    position: absolute; left: 0; right: 0; top: 130px; height: 74px;
    background: linear-gradient(180deg, var(--sky-light) 0%, var(--sky) 45%, var(--sky-deep) 100%);
    border-top: 3px solid #c9d3e0; border-bottom: 3px solid #c9d3e0;
    color: #fff; text-align: center; padding-top: 10px;
  }
  .band .person { font-weight: 700; font-size: 22px; line-height: 1.2; }
  .band .role { font-size: 15px; }
  .contact {
    position: absolute; left: 34px; right: 24px; top: 222px;
    color: var(--ink); font-size: 13px; line-height: 1.75;
  }
  .contact .address { padding-left: 120px; }
  .contact .key { color: var(--sky); font-weight: 700; }
  .contact .web { padding-left: 90px; }
</style>
</head>
<body>

  <section class="card card--back" aria-label="Appointment reminder side">
    <div class="watermark" aria-hidden="true"></div>
    <h2 class="appt-title">Next Appointment</h2>

    <div class="appt-row row-name">
      <span class="label">Name :</span><span class="line"></span>
      <span class="label">Time :</span><span class="line"></span><span class="ampm">AM/PM</span>
    </div>
    <div class="appt-row row-date">
      <span class="label">Date :</span><span class="line"></span>
    </div>
    <div class="appt-row row-days">
      <span class="day">Sun <span class="tick-box"></span></span>
      <span class="day">Mon <span class="tick-box"></span></span>
      <span class="day">Tue <span class="tick-box"></span></span>
      <span class="day">Wed <span class="tick-box"></span></span>
      <span class="day">Thu <span class="tick-box"></span></span>
      <span class="day">Fri <span class="tick-box"></span></span>
      <span class="day">Sat <span class="tick-box"></span></span>
    </div>
    <div class="appt-row row-note">
      <span class="label">Note :</span><span class="line"></span>
    </div>
    <div class="appt-row row-note2">
      <span class="line"></span>
    </div>
    <p class="appt-footnote">Please give us 24 hours notice if you need to change or cancel your appointment.</p>
  </section>

  <section class="card card--front" aria-label="Contact side">
    <div class="brand">
      <span class="dot" aria-hidden="true"></span>
      <span class="name">Harbourline Physiotherapy</span>
    </div>
    <div class="band">
      <div class="person">Daniel Hart</div>
      <div class="role">CEO/Founder</div>
    </div>
    <div class="contact">
      <div class="address">48 Wexford Lane Kellyvale NSW 2791</div>
      <div><span class="key">P:</span> 02 9481 2057 <span class="key">F:</span> 02 9481 2057 <span class="key">E:</span> info@harbourlinephysio.example.com.au</div>
      <div class="web"><span class="key">W:</span> www.harbourlinephysio.example.com.au</div>
    </div>
  </section>

</body>
</html>
```